Letterhead - Quarrington Law Group

I receive a fantastic logo from you guys and I'd like to incorporate it into business cards and letterhead. I accidentally approved design No. 32361474 and contacted designer Ravindra, and Ravindra sent me the zip folder for Design No. 32361417, which I very much appreciate.
I'd like to order business cards and letterhead with Design No. 32361417 as soon as possible, but I want to make sure that you incorporate the correct design (attached). I'd also like to provide my information to add (address, phone number, email, fax) but I'm not quite sure how to do it.
The information that I would like on the business cards and letterhead is as follows:
Quarrington Law Group
Theodore K. Quarrington, Esq.
2741 Hollis Avenue, Suite 520
San Francisco, CA 94087
Office: (415) 378-6130
Fax: (415) 746-0183
ted@quarringtonlawgroup-example.com
Thanks in advance for any guidance.
Ted Quarrington
Quarrington Law Group
(415) 831-4497 (cell)

```html
<!DOCTYPE html>
<html lang="en">
<head>
<meta charset="utf-8">
<title>Quarrington Law Group – Letterhead</title>
<link href="https://fonts.googleapis.com/css2?family=Cinzel:wght@600&family=Arimo&display=swap" rel="stylesheet">
<style>
  :root {
    --backdrop: #e1e1e1;
    --paper: #ffffff;
    --ink: #1c1b17;
    --muted: #808285;
    --accent: #1b8ac8;
  }
  html, body {
    margin: 0;
    padding: 0;
    width: 1200px;
    height: 1170px;
    overflow: hidden;
    background: var(--backdrop);
  }
  .letterhead {
    position: absolute;
    left: 240px;
    top: 75px;
    width: 721px;
    height: 1020px;
    background: var(--paper);
  }
  .masthead {
    position: absolute;
    top: 62px;
    left: 0;
    right: 0;
    text-align: center;
  }
  .firm-name {
    margin: 0;
    font-family: "Cinzel", "Times New Roman", serif;
    font-weight: 600;
    font-size: 27px;
    letter-spacing: 1.5px;
    color: var(--ink);
  }
  .footer {
    position: absolute;
    left: 0;
    right: 0;
    top: 936px;
    font-family: "Arimo", Arial, sans-serif;
    font-size: 12.5px;
    color: var(--muted);
  }
  .address {
    margin: 0;
    text-align: center;
    line-height: 20px;
  }
  .rule-accent {
    margin-top: 6px;
    height: 3px;
    background: var(--accent);
  }
  .rule-ink {
    margin-top: 3px;
    height: 1px;
    background: var(--ink);
  }
  .contact-row {
    display: flex;
    justify-content: center;
    align-items: center;
    gap: 16px;
    margin: 8px 0 0;
    padding: 0;
    list-style: none;
    line-height: 20px;
  }
  .contact-item {
    display: flex;
    align-items: center;
    gap: 6px;
  }
  .contact-icon {
    width: 12px;
    height: 12px;
    fill: var(--accent);
  }
</style>
</head>
<body>
  <main class="letterhead">
    <header class="masthead">
      <h1 class="firm-name">Quarrington Law Group</h1>
    </header>

    <footer class="footer">
      <p class="address">2741 Hollis Avenue, Suite 520, San Francisco, CA 94087</p>
      <div class="rule-accent"></div>
      <div class="rule-ink"></div>
      <ul class="contact-row">
        <li class="contact-item">
          <svg class="contact-icon" viewBox="0 0 24 24" aria-hidden="true">
            <path d="M6.6 10.8a15.1 15.1 0 0 0 6.6 6.6l2.2-2.2a1 1 0 0 1 1-.25 11.4 11.4 0 0 0 3.6.57 1 1 0 0 1 1 1V20a1 1 0 0 1-1 1A17 17 0 0 1 3 4a1 1 0 0 1 1-1h3.5a1 1 0 0 1 1 1c0 1.25.2 2.45.57 3.57a1 1 0 0 1-.25 1z"/>
          </svg>
          <span>(415) 378-6130</span>
        </li>
        <li class="contact-item">
          <svg class="contact-icon" viewBox="0 0 24 24" aria-hidden="true">
            <path d="M6 2h12v6H6zM3 9h18a1 1 0 0 1 1 1v9H2v-9a1 1 0 0 1 1-1zm5 4v4h8v-4z"/>
          </svg>
          <span>(415) 746-0183</span>
        </li>
        <li class="contact-item">
          <svg class="contact-icon" viewBox="0 0 24 24" aria-hidden="true">
            <path d="M2 5h20v14H2zm2 2v.3l8 5.5 8-5.5V7l-8 5.4z"/>
          </svg>
          <span>ted@quarringtonlawgroup-example.com</span>
        </li>
      </ul>
    </footer>
  </main>
</body>
</html>
```